Business Card Design Project

we are a new company , see www.chatharborlane.com
we also have a concurrent flyer deign competition so you may also wish to enter that.
We provide live customer support services for websites.
We cater for mainly european market.
info for card:
Martin Colbrook
Director
p: +353 (0)90 612 8051
f: +353 (0)90 612 8062
m: +353 (0)86 507 4926
e: martin@chatharborlane.com
w: www.chatharborlane.com
The card does not have to use the exact colour on the website but should ahve something of the general feel of it. It should have modern corporate feel without brash coulours. we will upload the logo and card should be standard european size 85x55mm
Target Market(s)
Online business owners
Industry/Entity Type
Business
Look and feel
Each slider illustrates characteristics of the customer's brand and the style your logo design should communicate.

```html
<!DOCTYPE html>
<html lang="en">
<head>
<meta charset="utf-8">
<title>Chat Harbor Lane – Business Card</title>
<link href="https://fonts.googleapis.com/css2?family=Roboto+Condensed:wght@700&family=Roboto:wght@400;700&display=swap" rel="stylesheet">
<style>
  :root {
    --backdrop: #3a3a3a;
    --card: #ffffff;
    --brand-grey: #6a6b6d;
    --brand-blue: #2a8fbd;
    --band-dark: #17698f;
    --band-light: #3fa6d2;
    --name-blue: #1d5f9e;
    --muted: #8a8a8a;
    --contact: #7a7a7a;
  }
  * { margin: 0; padding: 0; box-sizing: border-box; }
  html, body { width: 1200px; height: 900px; overflow: hidden; background: var(--backdrop); }
  .stage { position: relative; width: 1200px; height: 900px; }

  .card {
    position: absolute;
    background: var(--card);
    border-radius: 22px;
    overflow: hidden;
  }
  .card--front { left: 195px; top: 30px; width: 705px; height: 402px; }
  .card--back  { left: 200px; top: 468px; width: 700px; height: 384px; }

  .wordmark {
    position: absolute;
    display: flex;
    align-items: center;
    gap: 14px;
    font-family: "Roboto Condensed", sans-serif;
    font-weight: 700;
    color: var(--brand-grey);
    letter-spacing: 1px;
    white-space: nowrap;
  }
  .wordmark__square { background: var(--brand-blue); }
  .card--front .wordmark { left: 0; right: 0; justify-content: center; top: 118px; font-size: 58px; }
  .card--front .wordmark__square { width: 44px; height: 44px; }
  .card--back .wordmark { left: 28px; top: 40px; font-size: 38px; }
  .card--back .wordmark__square { width: 28px; height: 28px; }

  .tagline-band {
    position: absolute;
    left: 0; right: 0; top: 325px; height: 38px;
    background: linear-gradient(90deg, var(--band-dark), var(--band-light));
    display: flex; align-items: center; justify-content: center;
    font-family: "Roboto Condensed", sans-serif;
    font-weight: 700;
    font-size: 27px;
    color: #fff;
  }

  .person { position: absolute; right: 30px; top: 142px; text-align: right; font-family: "Roboto", sans-serif; }
  .person__name { font-size: 29px; font-weight: 700; color: var(--name-blue); line-height: 1.1; }
  .person__role { font-size: 20px; color: var(--muted); }

  .contacts { position: absolute; left: 28px; top: 248px; list-style: none; font-family: "Roboto", sans-serif; font-size: 19px; color: var(--contact); }
  .contacts li { display: flex; align-items: center; gap: 8px; height: 26px; }
  .contacts svg { width: 18px; height: 18px; fill: var(--name-blue); flex: none; }

  .footer-strip {
    position: absolute; left: 0; right: 0; bottom: 0; height: 10px;
    background: linear-gradient(90deg, #5fb6dc, var(--band-light));
  }
  .web-tab { position: absolute; right: 0; bottom: 0; width: 350px; height: 46px; }
  .web-tab svg { position: absolute; inset: 0; }
  .web-tab__url {
    position: absolute; right: 22px; top: 8px;
    font-family: "Roboto", sans-serif; font-weight: 700; font-size: 23px; color: #fff;
  }
</style>
</head>
<body>
<main class="stage">
  <section class="card card--front" aria-label="Card front">
    <div class="wordmark"><span>Chat Harbor Lane</span><span class="wordmark__square"></span></div>
    <div class="tagline-band">Live customer support online</div>
  </section>

  <section class="card card--back" aria-label="Card back">
    <div class="wordmark"><span>Chat Harbor Lane</span><span class="wordmark__square"></span></div>

    <div class="person">
      <div class="person__name">Martin Colbrook</div>
      <div class="person__role">Director</div>
    </div>

    <ul class="contacts">
      <li><svg viewBox="0 0 20 20"><path d="M2 8c0-3 4-5 8-5s8 2 8 5l-4 1-1-2H7L6 9 2 8zM5 10h10l2 7H3z"/></svg>+353 (0)90 612 8051</li>
      <li><svg viewBox="0 0 20 20"><path d="M5 2h9v5H5zM2 8h16v7H2zM4 15h12v3H4z"/></svg>+353 (0)90 612 8062</li>
      <li><svg viewBox="0 0 20 20"><path d="M6 1h8a1 1 0 0 1 1 1v16a1 1 0 0 1-1 1H6a1 1 0 0 1-1-1V2a1 1 0 0 1 1-1zm1 3v9h6V4z"/></svg>+353 (0)86 507 4926</li>
      <li><svg viewBox="0 0 20 20"><path d="M2 5h16v10H2zM3 6l7 5 7-5" /></svg>martin@chatharborlane.com</li>
    </ul>

    <div class="footer-strip"></div>
    <div class="web-tab">
      <svg viewBox="0 0 350 46" preserveAspectRatio="none">
        <defs>
          <linearGradient id="tabFill" x1="0" x2="1">
            <stop offset="0" stop-color="#17698f"/>
            <stop offset="1" stop-color="#3fa6d2"/>
          </linearGradient>
        </defs>
        <path d="M0 46 C20 46 22 0 48 0 H350 V46 Z" fill="url(#tabFill)"/>
      </svg>
      <span class="web-tab__url">www.chatharborlane.com</span>
    </div>
  </section>
</main>
</body>
</html>
```